Label Redesign For Hemp Oil Tincture Bottle*

I need a label redesigned for Marbleleaf Hemp, current bottle label and logo is attached. The current label doesn't standout, not sure if its the font size or colors on the existing label. It is very important to have on the label that this is a Premium Full Spectrum Hemp Oil that is 2000mg. Then after the label is redesigned and approved, I would need to packaging to be designed to match the approved label design.
This Hemp oil has a relaxing effect to help ease mental and emotional stress, tension and worry. The Omega Fatty Acids it contains also naturally improves your mood and overall brain function, causing you to feel more alert and focused. Hemp Oil helps with insomnia. Take some 2-3 hours before bedtime, you will feel relaxed yet aware of how tired you are that it will lead to a good night's sleep. Hemp Oil helps ease chronic pain and inflammation from conditions such as arthritis, fibromyalgia, lupus, and MS. As a pain relief supplement, it is a safer, natural, non-chemical and non-addictive alternative to prescription painkillers.

Target Market(s)

Adults

Industry/Entity Type

Supplement

Font styles to use
Serif
Sans Serif

Colors

Designer to choose colors to be used in the design.

Requirements
Must have
• All information thats on current label but where it says 750 in the front of the existing label, it needs to say 2000. The 2000 should be prominent on the label.

```html
<!DOCTYPE html>
<html lang="en">
<head>
<meta charset="utf-8">
<title>Marbleleaf Hemp – Tincture Label</title>
<link rel="stylesheet" href="https://fonts.googleapis.com/css2?family=Source+Sans+3:wght@400;600&family=Roboto:wght@400&display=swap">
<style>
  :root {
    --page: #ffffff;
    --label-green: #93c13d;
    --label-green-deep: #86b633;
    --brand-green: #3f6a1e;
    --band-dark: #3b3330;
    --band-text: #efeae6;
    --badge-red: #c9302a;
    --badge-text: #ffffff;
    --ink: #3a3632;
  }
  html, body {
    margin: 0;
    padding: 0;
    width: 1200px;
    height: 1200px;
    overflow: hidden;
    background: var(--page);
  }
  .canvas {
    position: relative;
    width: 1200px;
    height: 1200px;
  }
  .label {
    position: absolute;
    left: 188px;
    top: 60px;
    width: 824px;
    height: 1080px;
    background: linear-gradient(90deg, var(--label-green-deep), var(--label-green) 30%, var(--label-green) 70%, var(--label-green-deep));
    color: var(--ink);
    font-family: "Source Sans 3", sans-serif;
    text-align: center;
  }
  .brand-mark {
    position: absolute;
    top: 150px;
    left: 0;
    right: 0;
    display: flex;
    align-items: center;
    justify-content: center;
    gap: 22px;
  }
  .brand-dot {
    width: 64px;
    height: 64px;
    border-radius: 50%;
    background: var(--brand-green);
  }
  .brand-name {
    font-family: "Source Sans 3", sans-serif;
    font-weight: 600;
    font-size: 56px;
    color: var(--brand-green);
  }
  .title-band {
    position: absolute;
    top: 408px;
    left: 0;
    right: 0;
    height: 252px;
    background: var(--band-dark);
    color: var(--band-text);
    font-family: "Roboto", sans-serif;
    display: flex;
    flex-direction: column;
    justify-content: center;
    align-items: center;
    line-height: 1.05;
  }
  .band-brand {
    font-size: 42px;
    letter-spacing: 4px;
    margin-bottom: 30px;
  }
  .band-grade {
    font-size: 44px;
    letter-spacing: 4px;
  }
  .band-product {
    font-size: 38px;
    letter-spacing: 2px;
  }
  .strength-badge {
    position: absolute;
    top: 668px;
    left: 50%;
    transform: translateX(-50%);
    padding: 6px 22px;
    background: var(--badge-red);
    color: var(--badge-text);
    font-family: "Roboto", sans-serif;
    font-size: 54px;
    line-height: 1.1;
    border-radius: 8px;
  }
  .divider {
    position: absolute;
    top: 808px;
    left: 50%;
    width: 110px;
    height: 4px;
    margin-left: -55px;
    background: var(--ink);
  }
  .flavor {
    position: absolute;
    top: 830px;
    left: 0;
    right: 0;
    font-size: 44px;
    font-weight: 600;
  }
  .supplement {
    position: absolute;
    top: 925px;
    left: 0;
    right: 0;
    font-size: 40px;
    line-height: 1.35;
  }
</style>
</head>
<body>
  <main class="canvas">
    <section class="label">
      <div class="brand-mark">
        <span class="brand-dot"></span>
        <span class="brand-name">Marbleleaf Hemp</span>
      </div>
      <div class="title-band">
        <div class="band-brand">MARBLELEAF HEMP</div>
        <div class="band-grade">PREMIUN</div>
        <div class="band-grade">FULL SPECTRUM</div>
        <div class="band-product">2000 Hemp Oil</div>
      </div>
      <div class="strength-badge">2000mg</div>
      <div class="divider"></div>
      <div class="flavor">Natural Peppermint Flavor</div>
      <div class="supplement">
        <div>Dietary Supplement</div>
        <div>1 Fl. Oz (30ml )</div>
      </div>
    </section>
  </main>
</body>
</html>
```